Consultant Firm Marketing Flyer

I want to use this flyer to market health care consultant services. I would like a front and back glossy, professional, yet bold and eye catching design. I would like it to convey knowledge, expertise, partnership and strength. The colors should blue and white but I am very open to the designer being creative. You can visit my website to see colors and images I want to use at brightharborcare.net
I would like the home page image on my website to be incorporated into the flyer but I am also open to other images that work with the design. The designer can be creative.

I want to highlight 4 service area’s of focus to my clients:
1. Revenue Cycle Optimization (making my clients money)
2. Practice Management Optimization (improving clinical operations)
3. Health Compliance (following the law)
4. Health Care Technology: (Telemedicine and AI)
Please be creative. Go where ever your creativity leads.

```html
<!DOCTYPE html>
<html lang="en">
<head>
<meta charset="utf-8">
<title>Bright Harbor Health Partners – Flyer</title>
<link href="https://fonts.googleapis.com/css2?family=Didact+Gothic&family=Montserrat:wght@500;700;800&display=swap" rel="stylesheet">
<style>
:root{
  --blue:#0b4aa2;
  --blue-bright:#1a8fe0;
  --black:#151515;
  --grey-panel:#f2f2f3;
  --icon-grey:#8e8e8e;
  --text:#222;
  --white:#fff;
}
*{margin:0;padding:0;box-sizing:border-box}
html,body{width:1200px;height:1200px;overflow:hidden;background:var(--white)}
body{position:relative;font-family:"Didact Gothic",sans-serif;color:var(--text)}
.page{position:absolute;top:235px;width:516px;height:730px;overflow:hidden;background:var(--white)}
.page--front{left:54px}
.page--back{left:629px}
.abs{position:absolute}

/* front */
.hero-photo{left:0;top:0;width:516px;height:271px;background:linear-gradient(90deg,#b8bcc4 0%,#d9dce0 45%,#f4f5f6 68%,#fff 80%)}
.brand-name{right:22px;top:52px;width:190px;text-align:center;font-family:"Montserrat",sans-serif;font-weight:700;font-size:15px;line-height:1.25;color:var(--blue)}
.headline{right:22px;top:118px;text-align:right;font-family:"Didact Gothic",sans-serif;font-size:27px;line-height:33px;color:#111}
.headline strong{font-family:"Montserrat",sans-serif;font-weight:800;color:var(--blue);font-size:25px}
.welcome-band{left:0;top:271px;width:516px;height:82px;background:var(--blue);color:var(--white);text-align:center;padding-top:12px}
.welcome-band .lead{font-size:23px;line-height:28px}
.welcome-band .name{font-family:"Montserrat",sans-serif;font-weight:700;font-size:22px;line-height:30px}
.intro{left:20px;top:369px;width:476px;text-align:center;font-size:11px;line-height:13.6px}
.services{left:0;top:453px;width:516px;height:230px;background:var(--grey-panel)}
.services-title{left:0;top:16px;width:516px;text-align:center;font-family:"Montserrat",sans-serif;font-weight:800;font-size:22px;color:var(--blue)}
.service{display:flex;align-items:center;gap:14px;font-family:"Montserrat",sans-serif;font-weight:700;font-size:9.5px;line-height:11.5px;color:#111}
.service-icon{width:48px;height:48px;flex:none}
.divider{left:271px;top:62px;height:126px;border-left:2px dotted #555}
.footer-front{left:0;top:0;width:516px;height:730px}
.phone{left:22px;top:692px;font-family:"Montserrat",sans-serif;font-weight:700;font-size:20px;color:var(--white)}
.footer-rule{left:194px;top:690px;width:2px;height:30px;background:var(--white)}
.web{font-family:"Montserrat",sans-serif;font-weight:500;font-size:12px;letter-spacing:1.6px;color:var(--white)}
.web b{font-weight:700}

/* back */
.office-photo{left:0;top:0;width:516px;height:315px;background:linear-gradient(160deg,#e8ecef 0%,#c9cfd4 50%,#a99480 100%)}
.portrait-photo{left:262px;top:270px;width:254px;height:460px;background:linear-gradient(180deg,#5a3c2e 0%,#f1f1f1 35%,#e9eaec 100%)}
.badge{left:72px;top:238px;width:172px;height:172px}
.badge-name{left:84px;top:300px;width:148px;text-align:center;font-family:"Montserrat",sans-serif;font-weight:700;font-size:13px;line-height:16px;color:var(--white)}
.about-title{left:21px;top:437px;font-family:"Montserrat",sans-serif;font-weight:800;font-size:24px;color:var(--blue-bright);border-bottom:2px solid var(--blue-bright);padding-bottom:1px}
.about-text{left:21px;top:489px;width:236px;font-size:11px;line-height:13.7px}
</style>
</head>
<body>

<section class="page page--front">
  <div class="abs hero-photo" role="img" aria-label="Photo of a doctor and business colleagues meeting around a table in a bright office"></div>
  <div class="abs brand-name">Bright Harbor<br>Health Partners LLC</div>
  <h1 class="abs headline">ADVANCING<br><strong>HEALTHCARE</strong><br>OPERATIONS</h1>

  <div class="abs welcome-band">
    <div class="lead">Welcome To</div>
    <div class="name">Bright Harbor Health Partners</div>
  </div>

  <p class="abs intro">Bright Harbor Health Partners (BHP) is a healthcare consulting firm skilled at helping physician practices advance their strategic vision in an ever-evolving healthcare system. Bright Harbor Health Partners specializes in revenue cycle optimization, practice management improvement and developing new physician practices. Our technical skills allow us to dig deep into your revenue cycle while our strategic approach ensures we're keeping our eyes on the entire financial picture.</p>

  <div class="abs services">
    <h2 class="abs services-title">OUR SERVICES</h2>
    <div class="abs divider"></div>
    <div class="abs service" style="left:42px;top:60px">
      <svg class="service-icon" viewBox="0 0 48 48"><circle cx="24" cy="24" r="24" fill="var(--icon-grey)"/><circle cx="24" cy="24" r="12" fill="none" stroke="#fff" stroke-width="2.5"/><path d="M34 20l2 5 4-3" fill="none" stroke="#fff" stroke-width="2"/></svg>
      <span>Revenue Cycle Optimization<br>(making my clients money)</span>
    </div>
    <div class="abs service" style="left:291px;top:60px">
      <svg class="service-icon" viewBox="0 0 48 48"><circle cx="24" cy="24" r="24" fill="var(--icon-grey)"/><circle cx="24" cy="19" r="6" fill="none" stroke="#fff" stroke-width="2.5"/><path d="M11 28c4 6 8 8 13 8s9-2 13-8" fill="none" stroke="#fff" stroke-width="2.5"/></svg>
      <span>Health Care<br>Technology:<br>(Telemedicine and AI)</span>
    </div>
    <div class="abs service" style="left:42px;top:135px">
      <svg class="service-icon" viewBox="0 0 48 48"><circle cx="24" cy="24" r="24" fill="var(--icon-grey)"/><rect x="15" y="12" width="18" height="24" rx="2" fill="none" stroke="#fff" stroke-width="2.5"/><path d="M19 24l4 4 6-7" fill="none" stroke="#fff" stroke-width="2.5"/></svg>
      <span>Practice Management<br>Optimization<br>(improving clinical operations)</span>
    </div>
    <div class="abs service" style="left:291px;top:135px">
      <svg class="service-icon" viewBox="0 0 48 48"><circle cx="24" cy="24" r="24" fill="var(--icon-grey)"/><circle cx="24" cy="20" r="8" fill="none" stroke="#fff" stroke-width="2.5"/><path d="M14 36h20" stroke="#fff" stroke-width="2.5"/></svg>
      <span>Health Compliance<br>(following the law)</span>
    </div>
  </div>

  <svg class="abs footer-front" viewBox="0 0 516 730" aria-hidden="true">
    <path d="M0 650 Q300 670 516 610 L516 730 L0 730 Z" fill="var(--blue)"/>
    <path d="M0 660 Q300 680 516 628 L516 730 L0 730 Z" fill="var(--black)"/>
  </svg>
  <div class="abs phone">(555) 214-0188</div>
  <div class="abs footer-rule"></div>
  <div class="abs web" style="left:214px;top:698px">www.<b>brightharborcare</b>.net</div>
</section>

<section class="page page--back">
  <div class="abs office-photo" role="img" aria-label="Photo of two professionals reviewing documents at a laptop in a modern office"></div>
  <svg class="abs" style="left:0;top:0" width="516" height="730" viewBox="0 0 516 730" aria-hidden="true">
    <rect x="0" y="315" width="516" height="5" fill="var(--blue)"/>
    <path d="M0 615 Q160 655 330 655 L330 730 L0 730 Z" fill="var(--blue)"/>
    <path d="M0 628 Q160 668 330 668 L330 730 L0 730 Z" fill="var(--black)"/>
  </svg>
  <div class="abs portrait-photo" role="img" aria-label="Portrait photo of a smiling doctor in a white coat with a stethoscope holding a tablet"></div>
  <svg class="abs badge" viewBox="0 0 172 172" aria-hidden="true">
    <defs><radialGradient id="badgeFill" cx="50%" cy="40%" r="60%"><stop offset="0" stop-color="#2a9cf0"/><stop offset="1" stop-color="#0d56b8"/></radialGradient></defs>
    <circle cx="86" cy="86" r="84" fill="none" stroke="var(--blue)" stroke-width="2"/>
    <circle cx="86" cy="86" r="78" fill="var(--white)"/>
    <circle cx="86" cy="80" r="70" fill="url(#badgeFill)"/>
  </svg>
  <div class="abs badge-name">Bright Harbor<br>Health Partners LLC</div>
  <h2 class="abs about-title">About Us</h2>
  <p class="abs about-text">Bright Harbor Health Partners (BHP), founded in 2015, is a healthcare consulting firm skilled at helping physician practices advance their strategic vision in an ever-evolving healthcare system. Bright Harbor Health Partners specializes in revenue cycle optimization, practice management improvement and developing new physician practices.</p>
  <div class="abs web" style="left:21px;top:696px">www.<b>brightharborcare</b>.net</div>
</section>

</body>
</html>
```